Bag packaging design of sliced bread

The project is for design of line of sliced bread with different flavours. The brand of the bread will be "Velorasa". The shape of the bread will be oval. The bread will be packed in a bag. I attach the layout of the bag. The bag will be closed with a plastic clip. I attach images of similar products. The idea is to have one main design and then each colour to be different type of bread like those in the images 2 and 5.

```html
<!DOCTYPE html>
<html lang="en">
<head>
<meta charset="utf-8">
<title>Velorasa Sliced Bread – Bag Layout</title>
<link rel="stylesheet" href="https://fonts.googleapis.com/css2?family=Cinzel:wght@400;600&family=Ubuntu:wght@400&family=Arimo:wght@400&display=swap">
<style>
  :root {
    --paper: #ffffff;
    --cut-line: #29abe2;
    --guide: #3a3a3a;
    --brown: #6a4838;
    --orange: #f6a733;
    --ribbon: #c88028;
    --cream: #f2eae2;
    --crust: #f2ad48;
  }
  html, body {
    margin: 0;
    padding: 0;
    width: 1200px;
    height: 2473px;
    overflow: hidden;
    background: var(--paper);
  }
  .bag-layout { display: block; width: 1200px; height: 2473px; }
  .guide-line { stroke: var(--guide); stroke-width: 1.2; fill: none; }
  .guide-label {
    font-family: "Arimo", Arial, sans-serif;
    font-size: 15px;
    fill: #222;
  }
  .bag-outline { fill: none; stroke: var(--cut-line); stroke-width: 2; }
  .header-band { fill: var(--brown); }
  .header-stripe { fill: var(--orange); }
  .hang-hole { fill: var(--paper); stroke: var(--cut-line); stroke-width: 1.5; }
  .brand-name {
    font-family: "Cinzel", Georgia, serif;
    font-weight: 600;
    font-size: 64px;
    fill: var(--brown);
  }
  .product-title {
    font-family: "Cinzel", Georgia, serif;
    font-weight: 400;
    font-size: 124px;
    fill: #ffffff;
  }
  .product-claim {
    font-family: "Ubuntu", Arial, sans-serif;
    font-size: 46px;
    fill: #ffffff;
  }
</style>
</head>
<body>
<svg class="bag-layout" viewBox="0 0 1200 2473" xmlns="http://www.w3.org/2000/svg">
  <defs>
    <linearGradient id="loaf-tone" x1="0" y1="0" x2="0" y2="1">
      <stop offset="0" stop-color="#f2eae2"/>
      <stop offset="0.5" stop-color="#f2e6da"/>
      <stop offset="0.65" stop-color="#f4c987"/>
      <stop offset="1" stop-color="#f0a53a"/>
    </linearGradient>
    <linearGradient id="badge-tone" x1="0" y1="0" x2="0" y2="1">
      <stop offset="0" stop-color="#6a4838"/>
      <stop offset="0.68" stop-color="#6a4838"/>
      <stop offset="0.78" stop-color="#c88028"/>
      <stop offset="1" stop-color="#c88028"/>
    </linearGradient>
  </defs>

  <g class="dimension-guides">
    <line class="guide-line" x1="149" y1="59" x2="149" y2="2166"/>
    <line class="guide-line" x1="109" y1="81" x2="168" y2="81"/>
    <line class="guide-line" x1="109" y1="240" x2="168" y2="240"/>
    <line class="guide-line" x1="109" y1="2149" x2="168" y2="2149"/>
    <text class="guide-label" x="107" y="165" text-anchor="middle">40</text>
    <text class="guide-label" x="103" y="1200" text-anchor="middle">480</text>
    <line class="guide-line" x1="189" y1="2212" x2="1140" y2="2212"/>
    <line class="guide-line" x1="208" y1="2197" x2="208" y2="2256"/>
    <line class="guide-line" x1="1123" y1="2197" x2="1123" y2="2256"/>
    <text class="guide-label" x="665" y="2264" text-anchor="middle">230</text>
    <text class="guide-label" x="152" y="2377">230/480+40mm</text>
  </g>

  <rect class="bag-outline" x="208" y="81" width="915" height="2068"/>
  <rect class="header-band" x="208" y="81" width="915" height="159"/>
  <rect class="header-stripe" x="208" y="104" width="915" height="56"/>
  <circle class="hang-hole" cx="407" cy="160" r="39"/>
  <circle class="hang-hole" cx="924" cy="160" r="39"/>

  <rect class="loaf-art" role="img"
        aria-label="Illustration of a bread loaf with cream crumb, golden watercolour crust and wheat ears"
        x="299" y="384" width="714" height="1496" rx="60" fill="url(#loaf-tone)"/>

  <text class="brand-name" x="660" y="648" text-anchor="middle">Velorasa</text>

  <rect class="badge-art" role="img"
        aria-label="Scalloped brown title badge with orange edge over a curved ribbon banner"
        x="226" y="832" width="888" height="578" rx="40" fill="url(#badge-tone)"/>

  <text class="product-title" x="655" y="1051" text-anchor="middle" textLength="463" lengthAdjust="spacingAndGlyphs">SLICED</text>
  <text class="product-title" x="660" y="1201" text-anchor="middle" textLength="455" lengthAdjust="spacingAndGlyphs">BREAD</text>
  <text class="product-claim" x="653" y="1362" text-anchor="middle">100% natural</text>
</svg>
</body>
</html>
```